Aircraft Repair Station Supply Company Magnets for White Delivery Van

We need a design for some magnets we will use on our delivery van. The magnets are 18x24.

Our company sells aircraft consumables so we have discussed having it appear as aircraft rivets.

Information that should be included:

Company Name: Corvell Depot Supply
Company Website: www.82.corvell.example
Company Phone #: 212-555-0147

May include a descriptor: "QZR 82 Repair Station Supplies"

Visibility and Clarity are key: the magnets will be placed on a white van, but we want it to still pop. We have thought of something that may look like aluminum aircraft rivets.

Creativity that will attract the eyes of our clients.

Target Market(s)

Aircraft Repair Stations, people driving or citing van while making deliveries

Industry/Entity Type

It Company

Requirements
Must have
• Information that should be included:
• Company Name: Corvell Depot Supply
• Company Website: www.82.corvell.example
• Company Phone #: 212-555-0147
Nice to have
• May include a descriptor: "QZR 82 Repair Station Supplies"

```html
<!DOCTYPE html>
<html lang="en">
<head>
<meta charset="utf-8">
<title>Corvell Depot Supply – Van Magnet</title>
<link href="https://fonts.googleapis.com/css2?family=Michroma&family=Roboto:wght@400;500&display=swap" rel="stylesheet">
<style>
  :root {
    --metal-light: #e6e7e8;
    --metal-mid: #b9bbbd;
    --metal-dark: #8d9093;
    --ink: #141414;
    --screw-rim: #6f7275;
    --screw-face: #c9cbcd;
    --screw-slot: #3a3c3e;
  }
  html, body {
    margin: 0;
    padding: 0;
    width: 900px;
    height: 1200px;
    overflow: hidden;
    background: #ffffff;
  }
  .plate {
    position: relative;
    width: 900px;
    height: 1200px;
    overflow: hidden;
    background:
      radial-gradient(ellipse 70% 45% at 50% 35%, rgba(255,255,255,0.55), rgba(255,255,255,0) 70%),
      repeating-linear-gradient(180deg, rgba(255,255,255,0.18) 0 1px, rgba(0,0,0,0.06) 1px 2px, rgba(255,255,255,0) 2px 4px),
      repeating-linear-gradient(180deg, rgba(0,0,0,0.05) 0 3px, rgba(255,255,255,0.08) 3px 7px),
      linear-gradient(100deg, var(--metal-dark) 0%, var(--metal-mid) 22%, var(--metal-light) 48%, var(--metal-mid) 75%, var(--metal-dark) 100%);
  }
  .screw {
    position: absolute;
    width: 78px;
    height: 78px;
  }
  .screw--tl { left: 27px; top: 27px; }
  .screw--tr { right: 27px; top: 27px; }
  .screw--bl { left: 27px; bottom: 27px; }
  .screw--br { right: 27px; bottom: 27px; }

  .brand {
    position: absolute;
    left: 0;
    right: 0;
    top: 300px;
    text-align: center;
    color: var(--ink);
    font-family: "Michroma", sans-serif;
    font-weight: 400;
    text-transform: uppercase;
    margin: 0;
  }
  .brand__line {
    display: block;
  }
  .brand__line--main {
    font-size: 74px;
    letter-spacing: 18px;
    line-height: 1;
    padding-left: 18px;
  }
  .brand__line--sub {
    margin-top: 180px;
    font-size: 44px;
    letter-spacing: 8px;
    line-height: 1;
    padding-left: 8px;
  }
  .contact {
    position: absolute;
    left: 0;
    right: 0;
    top: 770px;
    margin: 0;
    padding: 0;
    list-style: none;
    display: flex;
    flex-direction: column;
    align-items: center;
    gap: 34px;
    font-family: "Roboto", sans-serif;
    font-weight: 500;
    color: var(--ink);
    font-size: 54px;
    line-height: 1;
  }
  .contact__item {
    display: flex;
    align-items: center;
    gap: 12px;
  }
  .contact__icon {
    width: 48px;
    height: 48px;
    flex: none;
  }
</style>
</head>
<body>
<main class="plate">
  <svg class="screw screw--tl" viewBox="0 0 78 78" aria-hidden="true">
    <circle cx="39" cy="39" r="37" fill="var(--screw-rim)"/>
    <circle cx="39" cy="39" r="33" fill="var(--screw-face)"/>
    <rect x="35" y="8" width="8" height="62" rx="2" fill="var(--screw-slot)" transform="rotate(-8 39 39)"/>
  </svg>
  <svg class="screw screw--tr" viewBox="0 0 78 78" aria-hidden="true">
    <circle cx="39" cy="39" r="37" fill="var(--screw-rim)"/>
    <circle cx="39" cy="39" r="33" fill="var(--screw-face)"/>
    <rect x="35" y="8" width="8" height="62" rx="2" fill="var(--screw-slot)" transform="rotate(10 39 39)"/>
  </svg>
  <svg class="screw screw--bl" viewBox="0 0 78 78" aria-hidden="true">
    <circle cx="39" cy="39" r="37" fill="var(--screw-rim)"/>
    <circle cx="39" cy="39" r="33" fill="var(--screw-face)"/>
    <rect x="35" y="8" width="8" height="62" rx="2" fill="var(--screw-slot)" transform="rotate(4 39 39)"/>
  </svg>
  <svg class="screw screw--br" viewBox="0 0 78 78" aria-hidden="true">
    <circle cx="39" cy="39" r="37" fill="var(--screw-rim)"/>
    <circle cx="39" cy="39" r="33" fill="var(--screw-face)"/>
    <rect x="35" y="8" width="8" height="62" rx="2" fill="var(--screw-slot)" transform="rotate(-6 39 39)"/>
  </svg>

  <h1 class="brand">
    <span class="brand__line brand__line--main">Corvell</span>
    <span class="brand__line brand__line--sub">Depot Supply</span>
  </h1>

  <ul class="contact">
    <li class="contact__item">
      <svg class="contact__icon" viewBox="0 0 48 48" aria-hidden="true">
        <circle cx="24" cy="24" r="23" fill="var(--ink)"/>
        <rect x="12" y="15" width="24" height="18" rx="2" fill="#ffffff"/>
        <path d="M12 17 L24 26 L36 17" fill="none" stroke="var(--ink)" stroke-width="2.5"/>
      </svg>
      <span>www.82.corvell.example</span>
    </li>
    <li class="contact__item">
      <svg class="contact__icon" viewBox="0 0 48 48" aria-hidden="true">
        <circle cx="24" cy="24" r="23" fill="var(--ink)"/>
        <path d="M17 12c1.5-1 3-.5 3.8 1l2 4c.6 1.3.2 2.6-.9 3.3l-1.6 1c1.2 2.8 3.3 4.9 6.1 6.1l1-1.6c.7-1.1 2-1.5 3.3-.9l4 2c1.5.8 2 2.3 1 3.8l-1.6 2.3c-1 1.4-2.8 2-4.5 1.5C21 32.8 15.2 27 13.5 18.4c-.4-1.7.2-3.5 1.5-4.5z" fill="#ffffff"/>
      </svg>
      <span>212-555-0147</span>
    </li>
  </ul>
</main>
</body>
</html>
```